College Social website needs a SIMPLE chart design

We need a simple one page website. The website is called "Fim-Bosk" a phonetic spelling of the word collage. The site allows users to gain up to date information on the nightlife and social scene of the campus. The site must be able to easily convey several key pieces of information; some type of grid/chart would work well.

This includes:
primary information:
-The name of the bar (about 9 bars on campus)
-The length of the line
-Guy/Girl ratio
-If there is cover (admittance fee) to enter the bar

secondary information:
-how packed/full the bar is
-if there is police raiding the bar
-a way to show more information including drink specials

would prefer a design similar to this page except more colorful/playful/fun: http://m.vantorelq.com/results.php

Some stylistic tips - the name of the service is called fim bosk. a phonetic spelling of collage (http://en.quorbinet.org/wiki/Collage). it doesnt need to look like a rainbow, just be exciting, engaging, and vivid.

look at this page for reference: http://www.plimvadee.com/blog/flat-ui-design-showcase/

other than the bar name and drink specials, everything should be presented graphically. All the bar stats are approximations and rough estimates, so you must find a way to present the information as relatives. historical information is not relevant. only the real time stats need to be included. here is a sample:

Bar name: Sample bar
guy/girl ratio: 70/30
line length: short
admittance fee: yes
bar attendance: near full
police raid: no
drink specials:
WINE NIGHT!
$8 BOTTLES OF GALLOWMERE WINE
$8 BOTTLES OF CHAMPAGNE
$2 TRESK PALE BOTTLES
$2 WELLS

Target Market(s)

target market for the site is 18-21 year olds in college.

Industry/Entity Type

College

Requirements
Must have
• the design MUST be mobile friendly. keep it simple. a flat design would be preferred.
the information must be conveyed in the form of symbols/icons. for instance, a pie chart to show guy/girl ratio.

```html
<!DOCTYPE html>
<html lang="en">
<head>
<meta charset="utf-8">
<title>Fim-Bosk</title>
<link rel="stylesheet" href="https://fonts.googleapis.com/css2?family=Roboto+Condensed:wght@400;700&display=swap">
<style>
  :root {
    --ink: #111111;
    --pink: #c8215a;
    --panel-grey: #d4d2d2;
    --band-grey: #d6d4d4;
    --row-alt: #f8f8f8;
    --muted: #c4c4c4;
    --rule: #9a9a9a;
    --dot: #7a7a7a;
    --figure-green: #2fb34a;
    --white: #ffffff;
  }
  * { box-sizing: border-box; margin: 0; padding: 0; }
  html, body { width: 900px; height: 1200px; overflow: hidden; background: var(--white); }
  body { font-family: "Roboto Condensed", "Arial Narrow", sans-serif; color: var(--ink); }
  .page { position: relative; width: 900px; height: 1200px; overflow: hidden; background: var(--white); }

  .site-header { position: absolute; top: 0; left: 0; width: 900px; height: 92px; border-bottom: 2px solid var(--rule); }
  .site-title { position: absolute; top: 14px; width: 100%; text-align: center; font-weight: 700; font-size: 56px; letter-spacing: -0.5px; line-height: 1; }
  .social-links { position: absolute; right: 44px; top: 68px; display: flex; gap: 12px; list-style: none; }
  .social-links li { width: 18px; height: 18px; border-radius: 50%; background: var(--ink); }

  .main-nav { position: absolute; top: 122px; left: 0; width: 900px; }
  .main-nav ul { list-style: none; position: relative; height: 26px; }
  .main-nav li { position: absolute; transform: translateX(-50%); font-size: 19px; white-space: nowrap; }
  .main-nav li.is-active { color: var(--pink); }

  .hero-collage { position: absolute; top: 164px; left: 0; width: 900px; height: 445px; }
  .hero-collage text { font-family: "Roboto Condensed", "Arial Narrow", sans-serif; }
  .panel-heading { font-weight: 700; font-size: 18px; fill: var(--pink); text-anchor: middle; }
  .panel-note { font-size: 9px; fill: var(--ink); text-anchor: middle; }
  .special-tag { font-size: 11px; fill: var(--white); text-anchor: middle; }
  .ratio-label { font-weight: 700; font-size: 12px; fill: var(--ink); text-anchor: middle; letter-spacing: 0.5px; }

  .slide-dots { position: absolute; top: 602px; left: 0; width: 900px; height: 12px; }
  .slide-dots span { position: absolute; width: 11px; height: 11px; border-radius: 50%; background: var(--dot); }
  .slide-dots span.is-current { background: var(--pink); }

  .bar-list { position: absolute; top: 668px; left: 0; width: 900px; list-style: none; }
  .bar-list::before { content: ""; position: absolute; top: -4px; left: 0; width: 100%; height: 4px; border-top: 1px dotted var(--rule); border-bottom: 1px dotted var(--rule); }
  .bar-item { height: 97px; padding: 20px 0 0 52px; }
  .bar-item + .bar-item { border-top: 3px dashed var(--rule); }
  .bar-item:nth-child(2) { background: var(--row-alt); }
  .bar-name { font-weight: 700; font-size: 22px; letter-spacing: 0.3px; }
  .bar-address { margin-top: 8px; font-size: 15px; color: var(--muted); letter-spacing: 0.5px; }

  .see-more { position: absolute; top: 958px; left: 0; width: 900px; height: 43px; background: var(--band-grey); color: var(--pink); text-align: center; font-weight: 700; font-size: 21px; line-height: 43px; letter-spacing: 0.5px; }

  .video-thumb { position: absolute; top: 1022px; left: 52px; width: 255px; height: 200px; background: linear-gradient(135deg, #4a1d7a 0%, #2c2aa8 45%, #3bb0d6 70%, #7a2a9a 100%); }
  .play-button { position: absolute; left: 98px; top: 50px; }

  .specials-info { position: absolute; top: 1018px; left: 553px; width: 300px; }
  .specials-info h2 { font-weight: 700; font-size: 21px; letter-spacing: 0.5px; }
  .specials-info p { margin-top: 8px; font-size: 16px; line-height: 31px; }
</style>
</head>
<body>
<div class="page">

  <header class="site-header">
    <h1 class="site-title">FIM-BOSK</h1>
    <ul class="social-links" aria-label="Social links">
      <li></li><li></li><li></li>
    </ul>
  </header>

  <nav class="main-nav">
    <ul>
      <li class="is-active" style="left:136px">HOME</li>
      <li style="left:243px">ABOUT US</li>
      <li style="left:364px">NIGHTLIFE</li>
      <li style="left:475px">EVENTS</li>
      <li style="left:601px">CONTACT US</li>
      <li style="left:743px">WHATS ON?</li>
    </ul>
  </nav>

  <svg class="hero-collage" viewBox="0 160 768 380" xmlns="http://www.w3.org/2000/svg">
    <defs>
      <linearGradient id="ratio-girls" x1="0" y1="0" x2="1" y2="1">
        <stop offset="0" stop-color="#5a2a5e"/>
        <stop offset="1" stop-color="#b0457e"/>
      </linearGradient>
      <clipPath id="ratio-clip">
        <polygon points="384,256 474,346 384,436 294,346"/>
      </clipPath>
    </defs>

    <g stroke="#ffffff" stroke-width="6">
      <polygon role="img" aria-label="Photo of a young man at the bar" points="212,178 264,230 212,282 160,230" fill="#8a5a45"/>
      <polygon role="img" aria-label="Photo of a woman laughing with friends" points="325,178 377,230 325,282 273,230" fill="#a8865a"/>
      <polygon role="img" aria-label="Photo of friends at a crowded bar" points="268,236 322,290 268,344 214,290" fill="#6e5a40"/>
      <polygon role="img" aria-label="Black and white photo of a guest drinking" points="450,176 504,230 450,284 396,230" fill="#4a4a4a"/>
      <polygon role="img" aria-label="Black and white photo of a bartender" points="558,176 612,230 558,284 504,230" fill="#8a8a8a"/>
      <polygon role="img" aria-label="Photo of champagne glasses" points="500,236 554,290 500,344 446,290" fill="#2a2a22"/>
      <polygon role="img" aria-label="Black and white photo of a dancing crowd" points="212,408 266,462 212,516 158,462" fill="#5a5a5a"/>
      <polygon role="img" aria-label="Tinted photo of a singer on stage" points="325,408 379,462 325,516 271,462" fill="#7a6a9a"/>
      <polygon role="img" aria-label="Black and white photo of raised hands" points="268,348 322,402 268,456 214,402" fill="#3a3a3a"/>
      <polygon role="img" aria-label="Photo of guests chatting in a busy room" points="440,408 494,462 440,516 386,462" fill="#7a4a2a"/>
      <polygon role="img" aria-label="Photo of friends smiling together" points="556,408 610,462 556,516 502,462" fill="#9a7a5a"/>
      <polygon role="img" aria-label="Photo of a packed bar room" points="500,348 554,402 500,456 446,402" fill="#5a3a22"/>
    </g>

    <!-- drink specials panel -->
    <polygon points="152,234 266,346 152,458 38,346" fill="var(--panel-grey)" stroke="#ffffff" stroke-width="6"/>
    <text class="panel-heading" x="149" y="286">DRINK</text>
    <text class="panel-heading" x="151" y="305">SPECIALS</text>
    <text class="panel-note" x="151" y="321">(NO POLICE RAID)</text>
    <rect x="65" y="337" width="168" height="19" fill="var(--pink)"/>
    <text class="special-tag" x="168" y="350">GALLOWMERE WINE</text>
    <rect x="97" y="375" width="100" height="19" fill="var(--pink)"/>
    <text class="special-tag" x="137" y="388">CHAMPAGNE</text>
    <rect role="img" aria-label="Two wine bottles" x="80" y="318" width="26" height="50" rx="4" fill="#2a2a2a"/>
    <rect role="img" aria-label="Champagne bottle" x="175" y="362" width="14" height="46" rx="4" fill="#3a4a2a"/>

    <!-- come and join panel -->
    <polygon points="620,234 732,346 620,458 508,346" fill="var(--panel-grey)" stroke="#ffffff" stroke-width="6"/>
    <text class="panel-heading" x="620" y="286">COME</text>
    <text class="panel-heading" x="622" y="305">AND JOIN</text>
    <text class="panel-note" x="622" y="321">(ADMITTANCE FEE &amp; SHORT LINE)</text>
    <rect x="538" y="337" width="168" height="19" fill="var(--pink)"/>
    <text class="special-tag" x="630" y="350">$2 TRESK PALE BOTTLES</text>
    <rect x="570" y="375" width="100" height="19" fill="var(--pink)"/>
    <text class="special-tag" x="636" y="388">$2 WELLS</text>
    <rect role="img" aria-label="Beer bottle" x="553" y="325" width="12" height="48" rx="4" fill="#4a3a22"/>
    <rect role="img" aria-label="Mixed drink glass" x="572" y="366" width="30" height="30" rx="4" fill="#8a8a8a"/>

    <!-- guy/girl ratio chart -->
    <polygon points="384,234 496,346 384,458 272,346" fill="#ffffff"/>
    <polygon points="384,242 488,346 384,450 280,346" fill="#111111"/>
    <g clip-path="url(#ratio-clip)">
      <rect x="290" y="250" width="82" height="200" fill="url(#ratio-girls)"/>
      <rect x="372" y="250" width="12" height="200" fill="#3cb6d2"/>
      <rect x="384" y="250" width="48" height="200" fill="#ff6a2a"/>
      <rect x="432" y="250" width="50" height="200" fill="#5a5a5a"/>
    </g>
    <rect x="347" y="305" width="75" height="18" fill="#ffffff"/>
    <text class="ratio-label" x="385" y="318">70% MALE</text>
    <rect x="311" y="349" width="78" height="18" fill="#ffffff"/>
    <text class="ratio-label" x="350" y="362">30% GIRL</text>
    <g fill="var(--figure-green)">
      <circle cx="428" cy="326" r="5"/>
      <polygon points="428,332 437,354 419,354"/>
      <rect x="423" y="354" width="3" height="14"/>
      <rect x="430" y="354" width="3" height="14"/>
      <circle cx="448" cy="326" r="5"/>
      <rect x="442" y="332" width="12" height="20" rx="2"/>
      <rect x="443" y="352" width="4" height="16"/>
      <rect x="449" y="352" width="4" height="16"/>
    </g>
  </svg>

  <div class="slide-dots" aria-label="Slides">
    <span style="left:404px"></span>
    <span class="is-current" style="left:429px"></span>
    <span style="left:454px"></span>
    <span style="left:481px"></span>
  </div>

  <ul class="bar-list">
    <li class="bar-item"><div class="bar-name">THE NAME OF THE BAR</div><div class="bar-address">ADDRESS</div></li>
    <li class="bar-item"><div class="bar-name">THE NAME OF THE BAR</div><div class="bar-address">ADDRESS</div></li>
    <li class="bar-item"><div class="bar-name">THE NAME OF THE BAR</div><div class="bar-address">ADDRESS</div></li>
  </ul>

  <div class="see-more">SEE MORE...</div>

  <div class="video-thumb" role="img" aria-label="Video still of a dance floor under blue and purple lights">
    <svg class="play-button" width="66" height="66" viewBox="0 0 66 66" xmlns="http://www.w3.org/2000/svg">
      <circle cx="33" cy="33" r="30" fill="#1d4fa8" stroke="#dfe6f2" stroke-width="5"/>
      <circle cx="33" cy="33" r="24" fill="#2a6ad0"/>
      <polygon points="26,20 48,33 26,46" fill="#ffffff"/>
    </svg>
  </div>

  <section class="specials-info">
    <h2>SPECIALS DATE &amp;&nbsp; PRICES INFO</h2>
    <p>"Lorem Ipsum is simply dummy text of the printing and typesetting industry. Lorem Ipsum has been the industry's standard dummy text ever since the 1500s.</p>
  </section>

</div>
</body>
</html>
```